Business Card Design

I need a card design for Melbourne based business in Australia, called T W Concrete Services. We Concrete and excavate. Concreteing is main part of business.Commercial ,Residential and industrial.We want to be known as T W C (services) as form of abbreviation.We would like to highlight the initials with contact phone. A clean straight edge design. We have no color preference and would prefer a design that can easily be used on all parts of our business including clothing,vechiles and stationary

Industry/Entity Type

Business

Contact Information for Business Card

Colin 0412 905 268
Barry 0421 574 360
twcsercices@quokkanet.com

```html
<!DOCTYPE html>
<html lang="en">
<head>
<meta charset="utf-8">
<title>T W C Services – Business Card</title>
<link rel="stylesheet" href="https://fonts.googleapis.com/css2?family=Montserrat:wght@400;500;600&family=Oswald:wght@400;600&family=Courier+Prime:wght@700&display=swap">
<style>
  :root {
    --backdrop: #e6e2dc;
    --concrete-light: #d9d9d9;
    --concrete-mid: #b4b4b4;
    --machine-grey: #6e6e6e;
    --band-black: #0c0c0c;
    --carbon: #2b2b2b;
    --carbon-deep: #1a1a1a;
    --accent: #f06a24;
    --slate: #3e3e3e;
    --white: #f2f2f2;
  }
  * { margin: 0; padding: 0; box-sizing: border-box; }
  html, body { width: 1200px; height: 1023px; overflow: hidden; }
  body {
    background: var(--backdrop);
    display: flex; align-items: center; justify-content: center;
  }
  .card {
    position: relative;
    width: 1000px; height: 572px;
    background: var(--carbon);
    overflow: hidden;
    box-shadow: 0 12px 30px rgba(0,0,0,.25);
  }
  .concrete-panel {
    position: absolute; left: 0; top: 0; width: 100%; height: 278px;
    background: radial-gradient(ellipse at 35% 45%, #e6e6e6 0%, var(--concrete-light) 45%, var(--concrete-mid) 100%);
  }
  .machine-photo {
    position: absolute; right: 0; top: 0; width: 400px; height: 278px;
    background: linear-gradient(90deg, rgba(110,110,110,0) 0%, rgba(110,110,110,.55) 30%, var(--machine-grey) 100%);
  }
  .brand {
    position: absolute; left: 70px; top: 70px;
    display: flex; align-items: center; gap: 22px;
  }
  .brand-initials, .brand-word {
    font-family: "Montserrat", sans-serif; font-weight: 500;
    color: var(--slate); letter-spacing: 4px;
  }
  .brand-initials { font-size: 96px; line-height: 1; }
  .brand-mark {
    width: 18px; height: 18px; background: var(--accent);
  }
  .brand-word { font-size: 52px; line-height: 1; }
  .tagline {
    position: absolute; left: 70px; top: 228px;
    font-family: "Montserrat", sans-serif; font-weight: 500;
    font-size: 27px; letter-spacing: 1.5px; color: var(--accent);
  }
  .band {
    position: absolute; left: 0; top: 278px; width: 100%; height: 26px;
    background: var(--band-black);
  }
  .contact-panel {
    position: absolute; left: 0; top: 304px; width: 100%; height: 268px;
    background: linear-gradient(180deg, var(--carbon) 0%, var(--carbon-deep) 100%);
  }
  .contacts {
    position: absolute; left: 330px; top: 340px;
    display: grid; grid-template-columns: auto 2px auto; column-gap: 22px;
  }
  .person { display: flex; flex-direction: column; gap: 16px; }
  .person-name {
    font-family: "Oswald", sans-serif; font-weight: 600;
    font-size: 34px; letter-spacing: 2px; color: var(--accent); line-height: 1;
  }
  .divider { background: var(--accent); }
  .phone {
    display: flex; align-items: center; gap: 12px;
    font-family: "Oswald", sans-serif; font-weight: 400;
    font-size: 30px; color: var(--white); letter-spacing: 1px; line-height: 1;
  }
  .phone-icon { width: 26px; height: 26px; }
  .email {
    position: absolute; left: 330px; top: 480px;
    font-family: "Courier Prime", monospace; font-weight: 700;
    font-size: 30px; color: var(--white); letter-spacing: 1px;
  }
</style>
</head>
<body>
  <div class="card">
    <div class="concrete-panel" role="img" aria-label="Grey concrete texture background"></div>
    <div class="machine-photo" role="img" aria-label="Photograph of an excavator working on site, in grey tones"></div>

    <div class="brand">
      <span class="brand-initials">T W C</span>
      <span class="brand-mark"></span>
      <span class="brand-word">SERVICES</span>
    </div>
    <p class="tagline">CONCRETE AND EXCAVATION</p>

    <div class="band"></div>
    <div class="contact-panel"></div>

    <div class="contacts">
      <div class="person">
        <span class="person-name">COLIN</span>
        <span class="phone">
          <svg class="phone-icon" viewBox="0 0 26 26" aria-hidden="true">
            <rect x="1" y="1" width="24" height="24" rx="4" fill="#f06a24"/>
            <rect x="8" y="5" width="10" height="16" rx="2" fill="none" stroke="#2b2b2b" stroke-width="2"/>
          </svg>
          0412 905 268
        </span>
      </div>
      <div class="divider"></div>
      <div class="person">
        <span class="person-name">BARRY</span>
        <span class="phone">
          <svg class="phone-icon" viewBox="0 0 26 26" aria-hidden="true">
            <rect x="1" y="1" width="24" height="24" rx="4" fill="#f06a24"/>
            <rect x="8" y="5" width="10" height="16" rx="2" fill="none" stroke="#2b2b2b" stroke-width="2"/>
          </svg>
          0421 574 360
        </span>
      </div>
    </div>
    <p class="email">twcsercices@quokkanet.com</p>
  </div>
</body>
</html>
```